Design a Business Card

I need a business card design, i cant decide between 3d design and special shaped card design so fell free to chose one or another to make a entry

Company name: "MARANTA STOC"
activity: "Materiale de constructii si finisaje"
adress: "Valea Verde Ionel Cazacu 82"
phone: "0741 903 618"
mail: "marantastoc@postaexemplu.ro"
company slogan (motto) "Casa ta, construita cu grija"

one side design only, u can make special shaped card like a hummingbird (maranta bird) or like a truck from image, also u can use colors from company logo, or you can try a 3d design with humming bird background.
If helps company profile is selling building materials (hardware store)

```html
<!DOCTYPE html>
<html lang="ro">
<head>
<meta charset="utf-8">
<title>Maranta Stoc – carte de vizită</title>
<link href="https://fonts.googleapis.com/css2?family=Roboto:wght@400;500;700;900&display=swap" rel="stylesheet">
<style>
  :root{
    --backdrop:#2a2a2a;
    --paper:#ffffff;
    --plum:#5b2a6e;
    --plum-light:#7a3b8f;
    --amber:#f2a33a;
    --teal:#2fa36b;
    --teal-light:#4cc488;
    --ink:#3b2546;
    --ink-soft:#b86a14;
  }
  *{box-sizing:border-box;margin:0;padding:0}
  html,body{width:1200px;height:900px;overflow:hidden}
  body{background:var(--backdrop);font-family:"Roboto",Arial,sans-serif;position:relative}
  .card{position:absolute;left:100px;top:164px;width:1000px;height:572px;background:var(--paper);overflow:hidden;box-shadow:0 10px 30px rgba(0,0,0,.45)}
  .card__shapes{position:absolute;inset:0}
  .brand{position:absolute;left:48px;top:78px;display:flex;align-items:center;gap:16px}
  .brand__dot{width:56px;height:56px;border-radius:50%;background:var(--teal)}
  .brand__name{font-size:66px;font-weight:700;color:var(--plum);line-height:1;letter-spacing:-1px}
  .slogan{position:absolute;left:48px;top:196px;font-size:24px;font-weight:900;color:var(--amber);letter-spacing:.3px}
  .company{position:absolute;left:48px;top:338px}
  .company__name{font-size:34px;font-weight:700;color:#fff;letter-spacing:.5px}
  .company__activity{margin-top:8px;font-size:18px;font-weight:700;color:var(--amber)}
  .contact{position:absolute;right:40px;top:270px;text-align:right}
  .contact__name{font-size:30px;font-weight:700;color:var(--plum)}
  .contact__role{font-size:17px;color:var(--ink-soft);margin-bottom:22px}
  .contact__line{display:flex;justify-content:flex-end;align-items:center;gap:12px;font-size:20px;color:var(--ink);height:46px}
  .contact__icon{width:26px;height:26px;flex:none}
</style>
</head>
<body>
<div class="card">
  <svg class="card__shapes" width="1000" height="572" viewBox="0 0 1000 572" aria-hidden="true">
    <defs>
      <linearGradient id="panelPlum" x1="0" x2="1" y1="0" y2="1">
        <stop offset="0" stop-color="#7a3b8f"/>
        <stop offset="1" stop-color="#4a2059"/>
      </linearGradient>
      <linearGradient id="cornerTeal" x1="0" x2="1" y1="0" y2="1">
        <stop offset="0" stop-color="#4cc488"/>
        <stop offset="1" stop-color="#23875a"/>
      </linearGradient>
    </defs>
    <polygon class="panel panel--base" points="0,300 560,300 440,572 0,572" fill="url(#panelPlum)"/>
    <polygon class="panel panel--accent" points="572,300 600,300 480,572 452,572" fill="#f2a33a"/>
    <polygon class="corner corner--accent" points="600,0 640,0 1000,218 1000,242" fill="#f2a33a"/>
    <polygon class="corner corner--base" points="640,0 1000,0 1000,218" fill="url(#cornerTeal)"/>
  </svg>

  <div class="brand">
    <span class="brand__dot"></span>
    <span class="brand__name">maranta</span>
  </div>
  <p class="slogan">CASA TA, CONSTRUITA CU GRIJA</p>
  <div class="company">
    <p class="company__name">MARANTA STOC</p>
    <p class="company__activity">MATERIALE DE CONSTRUCTII SI FINISAJE</p>
  </div>

  <div class="contact">
    <p class="contact__name">CLIENT NAME</p>
    <p class="contact__role">Designation</p>
    <p class="contact__line">0741 903 618
      <svg class="contact__icon" viewBox="0 0 26 26" aria-hidden="true"><circle cx="13" cy="13" r="12" fill="none" stroke="#f2a33a" stroke-width="2"/><path d="M8.5 7.5l3 0 1 3-1.6 1.2a8 8 0 0 0 3.4 3.4l1.2-1.6 3 1v3a1.5 1.5 0 0 1-1.6 1.4A11 11 0 0 1 7 9.1 1.5 1.5 0 0 1 8.5 7.5z" fill="#f2a33a"/></svg>
    </p>
    <p class="contact__line">marantastoc@postaexemplu.ro
      <svg class="contact__icon" viewBox="0 0 26 26" aria-hidden="true"><rect x="2" y="5" width="22" height="16" rx="2" fill="#f2a33a"/><path d="M3 6.5l10 7.5 10-7.5" fill="none" stroke="#fff" stroke-width="2"/></svg>
    </p>
    <p class="contact__line">Valea Verde Ionel Cazacu 82
      <svg class="contact__icon" viewBox="0 0 26 26" aria-hidden="true"><path d="M13 2a8 8 0 0 0-8 8c0 6 8 14 8 14s8-8 8-14a8 8 0 0 0-8-8z" fill="#f2a33a"/><circle cx="13" cy="10" r="3" fill="#fff"/></svg>
    </p>
  </div>
</div>
</body>
</html>
```